Cordova Exercise Phone Application Screen Design

We need a sharp professional design for a phone application. We specialize in Health and Fitness Software. This app will be a companion for www.VigorDeckNow.com.
We will be doing all backend and javascript work here and we need someone to create the HTML and CSS for the application which will be developed in Cordova.
For the contest we are submitting three screens. Once we award a winner we will give the winner the first oportunity to bid on the remaining 10 screens.
For the first step of the contest please do the page 1 and page 2 screen design, feel free to submit multiple designs. If we like your designs we will contact you and ask you to design the third page. Once that is done we would like to see the HTML and CSS for the three pages.
Page 1: Simple Home Page
Page 2: Client Search - The search is at the top and the results are below that. The Active | Inactive section is a selection (see https://quorblenet.com/radio-buttons-as-toggle-buttons-with-css/ for an example). Client A has their record expanded (that is what the triangle is). 136 stars should be 136 with Font-Awesome star after the number. To see what the graphs should look like please see the attached png. Then a list is below the stars and graphs.
Page 3/4: Step 1 of 3 - When the magnifying glass is selected a flyout with the search criteria comes out (page 3). Criteria is selected and the results are shown (page 4).
The default width should be 320 but the application should look good on all phones and tablets.
Please feel free to contact us with questions. The winner will get more work of a similar nature.

Target Market(s)
Physical Therapists
Colors
Designer to choose colors to be used in the design.
Requirements
Must have
- Clean and easy to understand design. Look professional and uncluttered. Be easy to understand and use. Must have the logo at the top (just the VDN logo is fine)
Should not have
- Cartoonish look and feel.

```html
<!DOCTYPE html>
<html lang="en">
<head>
<meta charset="utf-8">
<title>VigorDeck Now – App Screens</title>
<link href="https://fonts.googleapis.com/css2?family=Montserrat:wght@500;600;700&family=Open+Sans:wght@400;600&display=swap" rel="stylesheet">
<style>
:root{
  --stage:#e6e9e6;
  --green:#5ccb6f;
  --green-bright:#2fbd44;
  --dark:#232323;
  --panel:#3b3b3b;
  --panel-2:#2f2f2f;
  --row:#2b2b2b;
  --line:#4a4a4a;
  --red:#f3171c;
  --grey-btn:#5a5a5a;
  --white:#ffffff;
  --field:#ffffff;
  --muted:#cfcfcf;
}
*{box-sizing:border-box;margin:0;padding:0}
html,body{width:1200px;height:807px;overflow:hidden}
body{background:var(--stage);font-family:'Open Sans',sans-serif;color:var(--white);position:relative}
.screen{position:absolute;top:78px;width:300px;height:650px;background:var(--panel);overflow:hidden;border-radius:18px;box-shadow:0 10px 30px rgba(0,0,0,.18)}
.screen--home{left:105px}
.screen--search{left:450px}
.screen--program{left:795px;background:var(--dark)}
.app-bar{height:58px;background:var(--dark);display:flex;align-items:center;padding:0 12px;gap:12px}
.brand{font-family:'Montserrat',sans-serif;font-weight:700;font-size:19px;letter-spacing:1px;color:var(--white);display:flex;align-items:center;gap:8px}
.brand-box{width:12px;height:12px;background:var(--white)}
.app-title{font-family:'Montserrat',sans-serif;font-weight:700;font-size:17px;flex:1;text-align:center}
.help{margin-left:auto;width:36px;height:36px}
/* home */
.mail{margin:10px 0 0 10px;width:28px;height:22px;position:relative}
.badge{position:absolute;width:13px;height:13px;border-radius:50%;background:var(--red);font-size:8px;font-weight:600;display:flex;align-items:center;justify-content:center;left:7px;top:6px}
.menu{list-style:none;padding:10px 10px 0}
.menu-item{height:50px;background:var(--row);margin-bottom:10px;display:flex;align-items:center;gap:10px;padding:0 10px;font-size:12px;line-height:1.35}
.menu-item--active{background:linear-gradient(var(--green),var(--green-bright));font-family:'Montserrat',sans-serif;font-weight:700;font-size:14px;border:1px solid #8be39a}
.icon-disc{flex:none;width:34px;height:34px;border-radius:50%;background:var(--green);display:flex;align-items:center;justify-content:center}
.menu-item--active .icon-disc{background:var(--white)}
.menu-mail{margin-left:auto;position:relative;width:30px;height:22px}
/* search */
.search-form{margin:12px 12px 0;background:var(--panel-2);padding:14px 12px 20px}
.field{display:flex;align-items:center;justify-content:space-between;margin-bottom:8px;font-size:11px}
.field-input{width:160px;height:33px;background:var(--field);border:1px solid #999}
.toggle{display:flex;justify-content:flex-end;margin:8px 0 14px;font-size:12px}
.toggle span{padding:5px 10px}
.toggle .on{background:var(--red);font-weight:600}
.toggle .off{background:var(--grey-btn)}
.btn-search{display:block;width:100%;height:28px;background:var(--green);border-radius:3px;font-family:'Montserrat',sans-serif;font-size:14px;font-weight:500;text-align:center;line-height:28px}
.results{width:100%;border-collapse:collapse;font-size:9.5px;margin-top:12px}
.results th{font-family:'Montserrat',sans-serif;font-weight:600;font-size:9px;text-align:left;padding:10px 8px;background:var(--panel-2)}
.results td{padding:9px 8px;border-bottom:1px solid var(--line);background:var(--row)}
.results td+td{border-left:1px solid var(--line)}
.results .meta td{background:var(--panel);font-weight:600;border-left:none}
.results .issued td{background:var(--green);font-family:'Montserrat',sans-serif;font-weight:600;font-size:9px;border-left:none}
.results .sub td{background:var(--panel)}
.actions{display:inline-block;background:var(--white);color:#222;font-size:8.5px;padding:2px 6px;width:62px}
.actions::after{content:"▾";float:right}
.caret{color:var(--green);margin-left:4px}
/* program */
.step{background:var(--green);padding:12px 14px 14px;text-align:center;position:relative;height:126px}
.step-title{font-family:'Montserrat',sans-serif;font-weight:600;font-size:13px;line-height:1.45;letter-spacing:.3px}
.step-help{position:absolute;left:26px;top:58px;width:36px;height:36px}
.step-nav{display:flex;justify-content:center;margin:8px 0 0 50px;font-size:12px;font-weight:600}
.step-nav .cancel{background:var(--red);padding:4px 18px}
.step-nav .next{background:var(--grey-btn);padding:4px 14px}
.selected{margin-top:10px;font-size:11px;font-weight:600;display:flex;justify-content:center;align-items:center;gap:6px}
.search-for{display:flex;align-items:baseline;gap:16px;padding:22px 14px 0}
.search-for h2{font-family:'Montserrat',sans-serif;font-size:14px;color:var(--green);font-weight:600}
.search-for p{font-size:9.5px}
.pickers{display:flex;gap:14px;padding:24px 14px 0;font-size:11px}
.picker label{display:block;margin-bottom:6px}
.select{width:118px;height:28px;background:var(--white);color:#999;font-size:9.5px;line-height:28px;padding-left:8px;position:relative}
.select::after{content:"▾";position:absolute;right:0;top:0;width:24px;text-align:center;color:#333;border-left:1px solid #bbb}
.body-area{padding:22px 16px 0}
.body-area h3{font-family:'Montserrat',sans-serif;font-weight:500;font-size:15px;color:var(--green);margin-bottom:14px}
.area-list{list-style:none;display:grid;grid-template-columns:1fr 1fr;grid-auto-flow:column;grid-template-rows:repeat(7,23px);font-size:11px}
</style>
</head>
<body>

<svg width="0" height="0" style="position:absolute">
  <defs>
    <symbol id="help-diamond" viewBox="0 0 36 36">
      <rect x="7" y="7" width="22" height="22" transform="rotate(45 18 18)" fill="#5ccb6f"/>
      <circle cx="18" cy="18" r="8" fill="#fff"/>
      <text x="18" y="22" text-anchor="middle" font-family="Montserrat,sans-serif" font-weight="700" font-size="11" fill="#5ccb6f">?</text>
    </symbol>
    <symbol id="envelope" viewBox="0 0 28 22">
      <rect x="1" y="1" width="26" height="20" fill="#fff" stroke="#e33" stroke-width="1"/>
      <path d="M1 1 L14 12 L27 1" fill="none" stroke="#e33" stroke-width="1.5"/>
    </symbol>
  </defs>
</svg>

<!-- Home -->
<section class="screen screen--home" aria-label="Home screen">
  <header class="app-bar">
    <div class="brand"><span class="brand-box"></span>VDN</div>
    <svg class="help"><use href="#help-diamond"/></svg>
  </header>
  <div class="mail"><svg width="28" height="22"><use href="#envelope"/></svg><span class="badge">2</span></div>
  <ul class="menu">
    <li class="menu-item">
      <span class="icon-disc"><svg width="18" height="18" viewBox="0 0 18 18"><circle cx="7.5" cy="7.5" r="5" fill="none" stroke="#fff" stroke-width="2.4"/><path d="M11 11l5 5" stroke="#fff" stroke-width="2.6" stroke-linecap="round"/></svg></span>
      Search for Clients/Create Exercise Program
    </li>
    <li class="menu-item">
      <span class="icon-disc"><svg width="16" height="16" viewBox="0 0 16 16"><path d="M8 2v12M2 8h12" stroke="#fff" stroke-width="3"/></svg></span>
      Add Client
    </li>
    <li class="menu-item menu-item--active">
      <span class="icon-disc"><svg width="20" height="18" viewBox="0 0 20 18"><ellipse cx="10" cy="8" rx="8" ry="6.5" fill="#2fbd44"/><path d="M4 12l-2 5 6-3z" fill="#2fbd44"/></svg></span>
      Messages
      <span class="menu-mail"><svg width="30" height="22"><use href="#envelope"/></svg><span class="badge">2</span></span>
    </li>
    <li class="menu-item">
      <span class="icon-disc"><svg width="18" height="16" viewBox="0 0 18 16"><rect x="6.5" y="1" width="5" height="4" fill="#fff"/><rect x="1" y="11" width="5" height="4" fill="#fff"/><rect x="12" y="11" width="5" height="4" fill="#fff"/><path d="M9 5v3M3.5 11V8h11v3" fill="none" stroke="#fff" stroke-width="1.5"/></svg></span>
      Protocols
    </li>
    <li class="menu-item">
      <span class="icon-disc"><svg width="18" height="18" viewBox="0 0 18 18"><circle cx="9" cy="9" r="5.5" fill="none" stroke="#fff" stroke-width="3" stroke-dasharray="2.5 1.8"/><circle cx="9" cy="9" r="3.2" fill="none" stroke="#fff" stroke-width="2"/></svg></span>
      Settings
    </li>
  </ul>
</section>

<!-- Client search -->
<section class="screen screen--search" aria-label="Client search screen">
  <header class="app-bar">
    <div class="brand"><span class="brand-box"></span>VDN</div>
    <div class="app-title">Client Search</div>
    <svg class="help"><use href="#help-diamond"/></svg>
  </header>
  <form class="search-form">
    <div class="field"><span>First Name</span><span class="field-input"></span></div>
    <div class="field"><span>Last Name</span><span class="field-input"></span></div>
    <div class="field"><span>Client Id</span><span class="field-input"></span></div>
    <div class="field"><span>DOB</span><span class="field-input"></span></div>
    <div class="toggle"><span class="on">Active</span><span class="off">Inactive</span></div>
    <span class="btn-search">SEARCH</span>
  </form>
  <table class="results">
    <thead><tr><th>CLIENT NAME</th><th>CLIENT ID</th><th>DOB</th></tr></thead>
    <tbody>
      <tr><td>Client A</td><td>123abc</td><td>1/1/1979 <span class="caret">▴</span></td></tr>
      <tr class="meta"><td>136 ★</td><td colspan="2">Pain/Difficulty Graph</td></tr>
      <tr class="issued"><td>ISSUED</td><td colspan="2">EXPIRATION</td></tr>
      <tr class="sub"><td>1/1/2019</td><td>2/1/2019</td><td><span class="actions">Actions</span></td></tr>
      <tr class="sub"><td>12/1/2018</td><td>1/1/2019</td><td><span class="actions">Actions</span></td></tr>
      <tr><td>Client B</td><td>245abc</td><td>1/1/1969 <span class="caret">▾</span></td></tr>
      <tr><td>Client C</td><td>678abc</td><td>1/1/1989 <span class="caret">▾</span></td></tr>
    </tbody>
  </table>
</section>

<!-- Create program -->
<section class="screen screen--program" aria-label="Create exercise program screen">
  <header class="app-bar">
    <div class="brand"><span class="brand-box"></span>VDN</div>
    <div class="app-title">For Client A</div>
    <svg class="help" viewBox="0 0 36 36"><rect x="7" y="7" width="22" height="22" transform="rotate(45 18 18)" fill="#5ccb6f"/><circle cx="16.5" cy="16.5" r="5" fill="none" stroke="#fff" stroke-width="2.2"/><path d="M20 20l4 4" stroke="#fff" stroke-width="2.4" stroke-linecap="round"/></svg>
  </header>
  <div class="step">
    <div class="step-title">CREATE EXERCISE PROGRAM<br>STEP 1 OF 3</div>
    <svg class="step-help" viewBox="0 0 36 36"><rect x="7" y="7" width="22" height="22" transform="rotate(45 18 18)" fill="#fff"/><circle cx="18" cy="18" r="8" fill="#5ccb6f"/><text x="18" y="22" text-anchor="middle" font-family="Montserrat,sans-serif" font-weight="700" font-size="11" fill="#fff">?</text></svg>
    <div class="step-nav"><span class="cancel">Cancel</span><span class="next">Next &gt;&gt;</span></div>
    <div class="selected"><svg width="18" height="10" viewBox="0 0 18 10"><rect x="0" y="2" width="3" height="6" fill="#fff"/><rect x="3" y="0" width="3" height="10" fill="#fff"/><rect x="6" y="4" width="6" height="2" fill="#fff"/><rect x="12" y="0" width="3" height="10" fill="#fff"/><rect x="15" y="2" width="3" height="6" fill="#fff"/></svg>0 Exercises Selected</div>
  </div>
  <div class="search-for"><h2>SEARCH FOR</h2><p>Rapid | Protocols | Keyword</p></div>
  <div class="pickers">
    <div class="picker"><label>Libraries:</label><div class="select">General</div></div>
    <div class="picker"><label>Filters:</label><div class="select">All</div></div>
  </div>
  <div class="body-area">
    <h3>Body Area:</h3>
    <ul class="area-list">
      <li>Face/TMJ &gt;</li><li>Cervical &gt;</li><li>Thoracic &gt;</li><li>Lumbar &gt;</li><li>Abdominal &gt;</li><li>Sacroiliac &gt;</li><li>Hip &gt;</li>
      <li>Knee &gt;</li><li>Ankle/Foot &gt;</li><li>Shoulder &gt;</li><li>Elbow &gt;</li><li>Wrist/Hand &gt;</li><li>All Body &gt;</li>
    </ul>
  </div>
</section>

</body>
</html>
```